Harrowgate Estates Business Card for Apartment Buildings

Create business cards for resident managers who run apartment buildings. The audience is the public who are searching for apartment rentals, and current residents who live at the apartment building. Key design element will be incorporating the company logo, however, the logo cannot dominate. The building name and manager name are more important than the logo. Current business card design leaves little room for copy, so we may need to reduce the size on the current card to allow for more space for copy.

Target Market(s)

Adults 18-65 years of age, who are looking for an apartment rental, plus current residents who live at our apartment buildings.

Industry/Entity Type

Property Management

Contact Information for Business Card

A major design element will be use of the company logo. Important property and manager contact information must be part of the design. The size of the logo will need to be reduced to make room for building and manager contact copy.

Font styles to use
Sans Serif

Colors
3176b5
000000
959595
ffffff

Requirements
Must have
• 1) Incorporate the company logo.
• 2) Use the company colors (dark blue, black/grey, over white).
• 3) FEATURE THE BUILDING NAME
• 4) FEATURE THE MANAGER NAME
• 5) The company name is less important than BUILDING and MANAGER
• 6) Manager contact information
• **SEE ATTACHED CREATIVE BRIEF**
Nice to have
• 1) Back of card logo watermark
• 2) Ability to write notes on back of carfd
Should not have
• Avoid letting the company logo dominate the card, the building name and manager are more important than the company logo.

```html
<!DOCTYPE html>
<html lang="en">
<head>
<meta charset="utf-8">
<title>Harrowgate Estates – Resident Manager Business Card</title>
<link rel="stylesheet" href="https://fonts.googleapis.com/css2?family=Fira+Sans:wght@400;600;700&display=swap">
<style>
  :root {
    --brand-blue: #0b57a4;
    --brand-black: #1b1b1b;
    --brand-grey: #959595;
    --line-blue: #3176b5;
    --paper: #ffffff;
    --backdrop: #e8e8e5;
  }
  * { box-sizing: border-box; margin: 0; padding: 0; }
  html, body {
    width: 1200px; height: 800px; overflow: hidden;
    background: var(--backdrop);
    font-family: "Fira Sans", sans-serif;
  }
  .canvas { position: relative; width: 1200px; height: 800px; }
  .card {
    position: absolute; top: 245px;
    width: 540px; height: 309px;
    background: var(--paper);
    box-shadow: 0 6px 18px rgba(0,0,0,0.15);
    overflow: hidden;
  }
  .card--back { left: 40px; }
  .card--front { left: 620px; }

  /* Back: note lines + company name, kept apart */
  .notes {
    position: absolute; left: 42px; top: 48px; width: 215px;
  }
  .notes__line {
    height: 1px; background: var(--line-blue);
    margin-bottom: 30px;
  }
  .watermark {
    position: absolute; right: 28px; bottom: 84px;
    display: flex; align-items: center; gap: 9px;
    color: var(--brand-blue);
    font-weight: 700; font-size: 23px; letter-spacing: 0.3px;
    white-space: nowrap;
  }
  .mark-dot {
    width: 13px; height: 13px; border-radius: 50%;
    background: var(--brand-black); flex: none;
  }

  /* Front */
  .front__logo-panel {
    position: absolute; left: 0; top: 0; width: 312px; height: 100%;
    background: var(--paper);
  }
  .front__base-band {
    position: absolute; left: 0; bottom: 0; width: 312px; height: 46px;
    background: var(--brand-black);
  }
  .front__divider {
    position: absolute; left: 312px; top: 0; width: 8px; height: 100%;
    background: var(--brand-grey);
  }
  .company-name {
    position: absolute; left: 34px; top: 118px;
    display: flex; align-items: center; gap: 9px;
    color: var(--brand-blue);
    font-weight: 700; font-size: 23px; letter-spacing: 0.3px;
    white-space: nowrap;
  }
  .front__info {
    position: absolute; left: 320px; top: 0; right: 0; height: 100%;
    background: var(--brand-blue); color: var(--paper);
    padding: 40px 10px 0 22px;
  }
  .building {
    font-weight: 700; font-size: 15px; line-height: 1.3;
    margin-bottom: 14px;
  }
  .manager-name { font-weight: 700; font-size: 15px; line-height: 1.25; }
  .manager-title { font-weight: 400; font-size: 14px; margin-bottom: 4px; }
  .contact { font-size: 11px; line-height: 1.45; white-space: nowrap; }
</style>
</head>
<body>
<main class="canvas">

  <section class="card card--back" aria-label="Card back">
    <div class="notes">
      <div class="notes__line"></div>
      <div class="notes__line"></div>
      <div class="notes__line"></div>
      <div class="notes__line"></div>
      <div class="notes__line"></div>
      <div class="notes__line"></div>
      <div class="notes__line"></div>
    </div>
    <div class="watermark"><span class="mark-dot"></span>Harrowgate Estates</div>
  </section>

  <section class="card card--front" aria-label="Card front">
    <div class="front__logo-panel"></div>
    <div class="front__base-band"></div>
    <div class="front__divider"></div>
    <div class="company-name"><span class="mark-dot"></span>Harrowgate Estates</div>
    <div class="front__info">
      <p class="building">Linden Court Apartments<br>2845 Oakmere Avenue<br>Riverton, CA 90817</p>
      <p class="manager-name">Marisol Delgado</p>
      <p class="manager-title">Resident Manager</p>
      <p class="contact">
        Office: 555-210-4836<br>
        Fax: 555-210-4837<br>
        Cell: 555-384-9152<br>
        Email: marisol@harrowgateest.com
      </p>
    </div>
  </section>

</main>
</body>
</html>
```